Tree company needs modern website design

We need a website design for a tree company, here are some websites they like:

http://korvalemarine.com/company/ - we like the big image filling most of the page. Also the top half of the page looks good with the logo along top and good task bar also (we don’t like the spiel on left hand side covering up the picture + too many words!) If we could have our logo at lop like this along with our slogan which is 'Great Looking Trees that Grow Well'

http://www.pinecroftgardens.co.nz/ - we like the bottom half of this with the clean lines and welcome to part down bottom rather than the spiel to the left as on above site. Also like the moving leaves, any chance we could have birds such as a fantail, Tui and Bellbirds flying across the page and also some birdsong playing?

This is their existing website, that needs an updated design: http://tallfernwood.co.nz/

Industry/Entity Type

It Company

Font styles to use
Serif
Sans Serif

Requirements
Must have
• "Website by Pages Built Simple" located in bottom right hand side
Use images provided as background or banner images
Should not have
• Social Media icons

```html
<!DOCTYPE html>
<html lang="en">
<head>
<meta charset="utf-8">
<title>Tall Fernwood — Great Looking Trees that Grow Well</title>
<link rel="stylesheet" href="https://fonts.googleapis.com/css2?family=Arimo:wght@400;700&family=Cinzel:wght@600&family=Gelasio:wght@400&family=Open+Sans:wght@400;700&display=swap">
<style>
  :root{
    --teal:#0b6560;
    --teal-dark:#053a36;
    --footer:#04403c;
    --nav-text:#e6ef3c;
    --green:#3a9a2a;
    --slogan:#2f8a1e;
    --body:#444;
    --white:#fff;
    --rule:#a9a9a9;
  }
  *{box-sizing:border-box;margin:0;padding:0}
  html,body{width:894px;height:1200px;overflow:hidden}
  body{position:relative;background:linear-gradient(#dedede 622px,#f1f1f1 760px,#f7f7f7 1100px);font-family:"Arimo",Arial,sans-serif;color:var(--body)}
  .hero{position:absolute;left:0;top:0;width:894px;height:622px;
    background:linear-gradient(180deg,#7fa9d8 0%,#b9d1ec 20%,#cfd8dc 33%,#d9d2b8 42%,#cfc6a6 56%,#5f7b3c 64%,#4a5a36 70%,#8c8f8d 76%,#9d9f9d 88%,#7c7f7f 100%);
    box-shadow:0 6px 10px rgba(0,0,0,.12)}
  .site-header{position:absolute;left:15px;top:41px;width:865px;height:100px;border-radius:12px;background:rgba(255,255,255,.82)}
  .brand{position:absolute;left:12px;top:14px;display:flex;align-items:center;gap:7px;font-family:"Open Sans",sans-serif;font-weight:700;font-size:22px;color:var(--teal)}
  .brand-dot{width:14px;height:14px;border-radius:50%;background:var(--teal)}
  .slogan{position:absolute;right:14px;top:22px;font-family:"Cinzel",serif;font-weight:600;font-size:23px;color:var(--slogan);letter-spacing:.2px}
  .main-nav{position:absolute;left:7px;top:62px;width:851px;height:31px;border-radius:7px;background:var(--teal);display:flex;justify-content:space-around;align-items:center;padding:0 18px}
  .main-nav a{font-family:"Open Sans",sans-serif;font-weight:700;font-size:13px;color:var(--nav-text);text-decoration:none}
  .intro{position:absolute;left:24px;top:673px;width:456px}
  .intro h1{font-family:"Gelasio",serif;font-weight:400;font-size:21px;line-height:27px;color:var(--green);padding-bottom:8px;border-bottom:1px solid var(--rule)}
  .intro p{margin-top:16px;font-size:12px;line-height:15.3px;color:var(--body)}
  .projects{position:absolute;left:22px;top:855px;width:540px}
  .projects h2{font-family:"Gelasio",serif;font-weight:400;font-size:16px;color:var(--green);width:454px;padding-bottom:4px;border-bottom:1px solid var(--rule)}
  .project{position:absolute;top:33px;width:176px}
  .project h3{font-size:10.5px;line-height:13px;font-weight:700;color:#333}
  .project .thumb{display:block;margin-top:19px;width:91px;height:59px;background:linear-gradient(#7fa6d6 0%,#bcc7cc 35%,#3d4a52 62%,#5a8a3a 100%)}
  .project p{margin-top:18px;font-size:10.5px;line-height:13px;color:#333}
  .project a{display:block;margin-top:11px;font-size:11px;color:var(--teal);text-decoration:none}
  .quick-contact{position:absolute;left:583px;top:678px;width:289px;height:358px;border-radius:9px;background:var(--teal)}
  .quick-contact h2{position:absolute;left:19px;top:15px;font-family:"Gelasio",serif;font-weight:400;font-size:17px;color:var(--white)}
  .field{position:absolute;left:16px;width:255px;height:28px;border-radius:4px;background:var(--white);font-size:13px;color:var(--teal-dark);padding:6px 11px}
  .field.message{height:101px}
  .submit{position:absolute;left:15px;top:310px;width:256px;height:36px;border-radius:5px;background:var(--teal-dark);color:var(--white);font-size:13px;display:flex;align-items:center;justify-content:center}
  .treeline{position:absolute;left:258px;top:1106px;width:362px;height:39px;background:linear-gradient(rgba(4,64,60,0),rgba(4,64,60,.55) 35%,var(--footer))}
  .site-footer{position:absolute;left:0;top:1145px;width:894px;height:55px;background:var(--footer);display:flex;justify-content:center;align-items:center;gap:12px}
  .site-footer a{font-family:"Open Sans",sans-serif;font-size:12px;color:var(--white);text-decoration:none}
</style>
</head>
<body>
  <div class="hero" role="img" aria-label="Photo of a stadium and university building with newly planted semi mature trees along a paved walkway under a blue sky"></div>

  <header class="site-header">
    <div class="brand"><span class="brand-dot"></span>Tall Fernwood</div>
    <div class="slogan">Great Looking Trees that Grow Well</div>
    <nav class="main-nav">
      <a href="#">HOME</a><a href="#">ABOUT US</a><a href="#">TREE GALLERY</a><a href="#">PROJECTS</a><a href="#">CATALOGUE</a><a href="#">CONTACT</a>
    </nav>
  </header>

  <section class="intro">
    <h1>DO YOU NEED SEMI MATURE TREES FOR INSTANT EFFECT?</h1>
    <p>Most are available for immediate delivery New Zealand wide. All trees are grown in 100% Southland peat- a natural soil medium. They grow better and are lighter and easier to transport. Your tree requirements can be in large numbers of even grades. We offer contract growing of trees in advance for future projects. You can trust Tall Fernwood to deliver the goods and exceed your expectations.</p>
  </section>

  <section class="projects">
    <h2>PROJECTS</h2>
    <article class="project" style="left:2px">
      <h3>Harbourline Stadium &amp; Southgate University, Dunedin</h3>
      <span class="thumb" role="img" aria-label="Thumbnail photo of the stadium project"></span>
      <p>A prestigious project with scale and new edge architecture This project included plantings of ...</p>
      <a href="#">Read More</a>
    </article>
    <article class="project" style="left:181px">
      <h3>Harbourline Stadium &amp; Southgate University, Dunedin</h3>
      <span class="thumb" role="img" aria-label="Thumbnail photo of the stadium project"></span>
      <p>A prestigious project with scale and new edge architecture This project included plantings of ...</p>
      <a href="#">Read More</a>
    </article>
    <article class="project" style="left:357px">
      <h3>Harbourline Stadium &amp; Southgate University, Dunedin</h3>
      <span class="thumb" role="img" aria-label="Thumbnail photo of the stadium project"></span>
      <p>A prestigious project with scale and new edge architecture This project included plantings of ...</p>
      <a href="#">Read More</a>
    </article>
  </section>

  <aside class="quick-contact">
    <h2>QUICK CONTACT</h2>
    <div class="field" style="top:51px">Name *</div>
    <div class="field" style="top:88px">Phone Number</div>
    <div class="field" style="top:125px">Email *</div>
    <div class="field" style="top:163px">Subject</div>
    <div class="field message" style="top:200px">Message</div>
    <div class="submit">Submit</div>
  </aside>

  <div class="treeline" role="img" aria-label="Silhouette illustration of a row of trees above the footer"></div>
  <footer class="site-footer">
    <a href="#">HOME</a><a href="#">ABOUT US</a><a href="#">TREE GALLERY</a><a href="#">PROJECTS</a><a href="#">CATALOGUE</a><a href="#">CONTACT</a>
  </footer>
</body>
</html>
```